business card and flyer/pricelist

Business Name: Fern Locks Westbrook
new boutique salon run from home, using Australian owned natural products and colours, we need a flyer design to do a letter box drop to advertise the business as well as incorporating a price list on the front (single sided with writing on front and only colour on back)

The salon has a natural feel with light coloured timber chairs, bamboo timber bench top and shelving.

we are after a natural toned colour for the flyer, with possibly a brown/darkish colour writing

we are after a flyer that will also be able to use the design heading (business name) for business cards as well

feel free to look on my pintrest account to get a feel for my style under Marla Quenby.

I love simple clean and Natural looks.

Font styles to use
Script
Other font styles liked:
• SCRIPT HANDWRITTEN FONTS

Colors
cadf82
e9f1ce
5c5c5c
d3d3d3
add136
fee18a

Requirements
Must have
• NATURAL COLOURINGS, eg soft greens, browns,
white or off white background.
Should not have
• photos,

```html
<!DOCTYPE html>
<html lang="en">
<head>
<meta charset="utf-8">
<title>Fern Locks Westbrook – Flyer &amp; Price List</title>
<link rel="stylesheet" href="https://fonts.googleapis.com/css2?family=Jost:wght@400;500&family=Great+Vibes&display=swap">
<style>
  :root {
    --page: #fdfcf7;
    --leaf: #add136;
    --leaf-soft: #cadf82;
    --leaf-pale: #e9f1ce;
    --sun: #fee18a;
    --bark: #5a4330;
    --bark-deep: #3f2f22;
    --stone: #5c5c5c;
    --mist: #d3d3d3;
  }
  * { margin: 0; padding: 0; box-sizing: border-box; }
  html, body {
    width: 1200px;
    height: 2609px;
    overflow: hidden;
    background: var(--page);
    font-family: "Jost", sans-serif;
    color: var(--bark);
  }
  .flyer {
    position: relative;
    width: 1200px;
    height: 2609px;
    background: var(--page);
  }
  .masthead {
    position: absolute;
    left: 43px;
    top: 46px;
    width: 1100px;
    height: 300px;
    border-radius: 24px 24px 0 0;
    background:
      radial-gradient(ellipse 420px 200px at 22% 100%, var(--leaf-pale) 0%, rgba(233,241,206,0) 100%),
      linear-gradient(180deg, var(--leaf-soft) 0%, var(--leaf) 100%);
    display: flex;
    align-items: center;
    justify-content: center;
    overflow: hidden;
  }
  .business-name {
    font-weight: 500;
    color: var(--bark-deep);
    letter-spacing: -1px;
    white-space: nowrap;
  }
  .masthead .business-name { font-size: 96px; }

  .price-list {
    position: absolute;
    left: 143px;
    top: 420px;
    width: 900px;
  }
  .price-title {
    font-family: "Great Vibes", cursive;
    font-weight: 400;
    font-size: 150px;
    line-height: 170px;
    text-align: center;
    color: var(--bark);
    margin-bottom: 40px;
  }
  .price-group { margin-bottom: 60px; }
  .group-title {
    font-family: "Great Vibes", cursive;
    font-weight: 400;
    font-size: 96px;
    line-height: 110px;
    color: var(--bark);
    border-bottom: 3px solid var(--leaf-soft);
    margin-bottom: 20px;
  }
  .price-row {
    display: flex;
    align-items: baseline;
    font-size: 46px;
    line-height: 76px;
    color: var(--stone);
  }
  .price-row .service { white-space: nowrap; }
  .price-row .leader {
    flex: 1;
    border-bottom: 4px dotted var(--mist);
    margin: 0 18px;
  }
  .price-row .cost { color: var(--bark); font-weight: 500; }

  .contact-band {
    position: absolute;
    left: 43px;
    top: 2252px;
    width: 1100px;
    height: 231px;
    background: var(--leaf-pale);
    color: var(--bark);
    font-size: 58px;
    line-height: 62px;
    letter-spacing: -1px;
  }
  .contact-owner { position: absolute; left: 58px; top: 24px; }
  .contact-reach { position: absolute; right: 40px; top: 24px; text-align: center; }
  .sign-off {
    position: absolute;
    left: 43px;
    top: 2483px;
    width: 1100px;
    height: 100px;
    border-radius: 0 0 24px 24px;
    background:
      radial-gradient(ellipse 380px 90px at 78% 50%, var(--sun) 0%, rgba(254,225,138,0) 100%),
      linear-gradient(180deg, var(--leaf), var(--leaf-soft));
    display: flex;
    align-items: center;
    justify-content: center;
  }
  .sign-off .business-name { font-size: 54px; }
</style>
</head>
<body>
  <main class="flyer">
    <header class="masthead">
      <h1 class="business-name">Fern Locks Westbrook</h1>
    </header>

    <section class="price-list">
      <h2 class="price-title">Price List</h2>

      <div class="price-group">
        <h3 class="group-title">Cuts</h3>
        <p class="price-row"><span class="service">Ladies Cut &amp; Blow Dry</span><span class="leader"></span><span class="cost">$55</span></p>
        <p class="price-row"><span class="service">Men's Cut</span><span class="leader"></span><span class="cost">$28</span></p>
        <p class="price-row"><span class="service">Children's Cut</span><span class="leader"></span><span class="cost">$20</span></p>
      </div>

      <div class="price-group">
        <h3 class="group-title">Colour</h3>
        <p class="price-row"><span class="service">Full Head Colour</span><span class="leader"></span><span class="cost">$85</span></p>
        <p class="price-row"><span class="service">Regrowth Colour</span><span class="leader"></span><span class="cost">$70</span></p>
        <p class="price-row"><span class="service">Half Head Foils</span><span class="leader"></span><span class="cost">$95</span></p>
        <p class="price-row"><span class="service">Toner</span><span class="leader"></span><span class="cost">$30</span></p>
      </div>

      <div class="price-group">
        <h3 class="group-title">Styling</h3>
        <p class="price-row"><span class="service">Blow Dry</span><span class="leader"></span><span class="cost">$35</span></p>
        <p class="price-row"><span class="service">Upstyle</span><span class="leader"></span><span class="cost">$65</span></p>
      </div>
    </section>

    <section class="contact-band">
      <div class="contact-owner">
        <p>Owners Name</p>
        <p>Address</p>
      </div>
      <div class="contact-reach">
        <p>Phone: 123456</p>
        <p>email@website.com</p>
      </div>
    </section>

    <footer class="sign-off">
      <p class="business-name">Fern Locks Westbrook</p>
    </footer>
  </main>
</body>
</html>
```